Dr. Calvin Oberlake personal brand website

I need a new website for a client who is in a speaker, author, and consultant in the mental health space.

Dr. Oberlake is a mental healthcare speaker, author, coach, and consultant who has worked with clients at the local and state levels.

His website will be used to market him for speaking and media opportunities, as well as to inform potential consulting clients.

Included with the uploaded files is a brand strategy document that outlines how Dr. Oberlake's personal brand will be positioned in the marketplace.

Examples of websites to draw inspiration from:
https://www.marktenbrook.example
https://drkarenwolstad.example
http://nadiafrenk.example/

Pages:
Meet The Doctor (bio is included with uploaded files)
The Book (picture of the book is included)
Speaking
Consulting (include link to https://kvtrmgx.example/)
Contact

Target Market(s)

Mental Health/Substance Abuse Recovery

Industry/Entity Type

Mental Health

Coding

Coded - Design and coding required

Number of Pages Required

5+ page

Font styles to use
Sans Serif

Colors

Designer to choose colors to be used in the design.

Requirements
Must have
• Popup optin form to capture email addresses.
Should not have
• no clipart or stock images

```html
<!DOCTYPE html>
<html lang="en">
<head>
<meta charset="utf-8">
<title>Dr. Calvin Oberlake</title>
<link href="https://fonts.googleapis.com/css2?family=Poppins:wght@400;500;600&display=swap" rel="stylesheet">
<style>
:root{
  --blue:#1157c4;
  --blue-light:#3a74e8;
  --ink:#111;
  --text:#333;
  --muted:#666;
  --white:#fff;
  --footer:#242424;
  --footer-bottom:#141414;
}
*{margin:0;padding:0;box-sizing:border-box}
html,body{width:1200px;height:2233px;overflow:hidden}
body{font-family:'Poppins',sans-serif;color:var(--text);background:var(--white);position:relative}
.abs{position:absolute}

/* header */
.site-header{left:0;top:0;width:1200px;height:52px;background:var(--white);border-bottom:1px solid #e3e3e3}
.brand{left:197px;top:9px;display:flex;align-items:center;gap:8px;font-size:15px;font-weight:500;color:var(--ink)}
.brand-dot{width:33px;height:33px;border-radius:50%;background:var(--blue)}
.main-nav{right:197px;top:0;display:flex;height:52px}
.main-nav a{font-size:11px;color:var(--ink);text-decoration:none;padding:0 12px;line-height:50px;position:relative}
.main-nav a.active{color:var(--blue)}
.main-nav a.active::after{content:"";position:absolute;left:0;right:0;bottom:-1px;height:3px;background:var(--blue)}

/* hero */
.hero{left:0;top:52px;width:1200px;height:421px;background:linear-gradient(90deg,#dcdcdc,#f2f2f2 40%,#e6e6e6 75%,#d8d8d8)}
.hero-portrait{left:712px;top:36px;width:232px;height:385px;background:linear-gradient(180deg,#3a3f4c,#20242e);border-radius:90px 90px 0 0}
.hero-card{left:198px;top:108px;width:445px;height:151px;background:linear-gradient(90deg,#fff 80%,rgba(255,255,255,0))}
.hero-tag{left:17px;top:19px;width:200px;height:32px;background:linear-gradient(90deg,var(--blue),#5b8cef 75%,rgba(91,140,239,0));color:var(--white);font-size:16px;font-weight:600;line-height:32px;padding-left:9px}
.hero-title{left:15px;top:52px;font-size:33px;font-weight:500;color:var(--ink);white-space:nowrap}
.hero-sub{left:15px;top:94px;font-size:31px;font-weight:500;color:var(--blue);white-space:nowrap}
.btn{display:block;background:var(--ink);color:var(--white);text-align:center;text-decoration:none;border:2px solid #fff;box-shadow:0 0 0 1px #999}
.hero-btn{left:198px;top:276px;width:135px;height:29px;font-size:15px;line-height:25px}
.slider-arrow{width:28px;height:28px;border-radius:50%;background:var(--white);box-shadow:0 1px 4px rgba(0,0,0,.25)}
.slider-arrow svg{display:block}

/* consultation */
.consult{left:0;top:473px;width:1200px;height:204px;background:linear-gradient(180deg,#0d55be,#3a74e8)}
.consult h2{position:absolute;left:0;width:1200px;top:20px;text-align:center;color:var(--white);font-size:19px;font-weight:500}
.consult .rule{left:554px;top:63px;width:92px;height:2px;background:var(--white)}
.field label{display:block;font-size:10.5px;color:var(--white);margin-bottom:6px}
.field span{display:block;width:163px;height:27px;background:var(--white);border:1px solid #c8d4ee}
.submit{left:526px;top:160px;width:148px;height:24px;font-size:12px;line-height:20px;font-weight:500}

/* about */
.about-deco{left:-25px;top:858px;width:260px;height:260px;border-radius:50%;background:radial-gradient(circle,#f3f3f3,#f7f7f7 70%,rgba(255,255,255,0))}
.about-frame{left:198px;top:740px;width:320px;height:295px;background:linear-gradient(180deg,var(--blue),var(--blue-light))}
.about-photo{left:208px;top:725px;width:323px;height:300px;background:linear-gradient(90deg,#ececef 30%,#5a4037 60%,#2b2524)}
.eyebrow{font-size:17px;color:var(--ink)}
.about-text{left:589px;top:726px;width:410px}
.about-text h3{font-size:27px;font-weight:500;color:var(--blue);margin:8px 0 16px}
.body-copy{font-size:10.5px;line-height:21px;color:var(--text)}
.signature{left:589px;top:978px;width:200px;height:32px;background:linear-gradient(90deg,#e4e4e4,#f4f4f4)}

/* book */
.book{left:0;top:1099px;width:1200px;height:423px;background:linear-gradient(110deg,#dedcd6,#d3d1cb 60%,#cac8c2)}
.book-text{left:198px;top:74px;width:410px}
.book-text h3{font-size:27px;font-weight:500;color:var(--ink);margin:8px 0 16px;white-space:nowrap}
.book-btn{left:198px;top:326px;width:148px;height:31px;font-size:12px;line-height:27px;font-weight:500}
.book-visual{left:655px;top:64px;width:500px;height:305px;background:linear-gradient(135deg,#cfc7ad,#9eaecf 50%,#c7c9ce);border-radius:6px}

/* blogs */
.blogs-title{left:0;width:1200px;top:1564px;text-align:center;font-size:22px;font-weight:500;color:var(--blue)}
.blogs-rule{left:562px;top:1609px;width:76px;height:2px;background:var(--blue)}
.blog-card{top:1638px;width:242px;height:273px;border:1px solid #e8e8e8;background:#fafafa}
.blog-img{width:240px;height:166px}
.blog-card h4{font-size:14.5px;font-weight:600;color:var(--blue);line-height:17px;padding:12px 12px 0}
.blog-card p{font-size:9.5px;color:#777;line-height:11.5px;padding:10px 12px 0}

/* footer */
.site-footer{left:0;top:1965px;width:1200px;height:218px;background:var(--footer);color:var(--white)}
.footer-brand{left:197px;top:38px;display:flex;align-items:center;gap:8px;font-size:14px;font-weight:500}
.footer-brand .brand-dot{width:32px;height:32px;background:var(--white)}
.footer-about{left:198px;top:93px;width:230px;font-size:9px;line-height:12.5px}
.footer-col{top:54px}
.footer-col h5{font-size:10.5px;font-weight:600;margin-bottom:11px}
.footer-col li{list-style:none;font-size:10.5px;line-height:13.8px;white-space:nowrap}
.copyright{left:0;top:2183px;width:1200px;height:50px;background:var(--footer-bottom);color:var(--white);font-size:11px;text-align:center;line-height:50px}
</style>
</head>
<body>

<header class="site-header abs">
  <div class="brand abs"><span class="brand-dot"></span>Dr. Calvin Oberlake</div>
  <nav class="main-nav abs">
    <a href="#" class="active">Home</a>
    <a href="#">Meet The Doctor</a>
    <a href="#">The Book</a>
    <a href="#">Speaking</a>
    <a href="#">Consulting</a>
    <a href="#" style="padding-right:0">Contact</a>
  </nav>
</header>

<section class="hero abs">
  <div class="hero-portrait abs" role="img" aria-label="Portrait of Dr. Calvin Oberlake in a pinstripe suit"></div>
  <div class="hero-card abs">
    <div class="hero-tag abs">MEET THE DOCTOR</div>
    <div class="hero-title abs">Dr. Calvin Oberlake</div>
    <div class="hero-sub abs">Founder of KVRHS</div>
  </div>
  <a href="#" class="btn hero-btn abs">READ MORE</a>
  <div class="slider-arrow abs" style="left:15px;top:185px"><svg width="28" height="28"><path d="M16 9l-5 5 5 5" fill="none" stroke="#111" stroke-width="2"/></svg></div>
  <div class="slider-arrow abs" style="left:1152px;top:185px"><svg width="28" height="28"><path d="M12 9l5 5-5 5" fill="none" stroke="#111" stroke-width="2"/></svg></div>
</section>

<section class="consult abs">
  <h2>Request a Constultation</h2>
  <div class="rule abs"></div>
  <div class="field abs" style="left:237px;top:82px"><label>First Name</label><span></span></div>
  <div class="field abs" style="left:424px;top:82px"><label>Last Name</label><span></span></div>
  <div class="field abs" style="left:611px;top:82px"><label>Email Address</label><span></span></div>
  <div class="field abs" style="left:798px;top:82px"><label>Phone Number</label><span></span></div>
  <a href="#" class="btn submit abs">SUBMIT</a>
</section>

<section class="about">
  <div class="about-deco abs" role="img" aria-label="Faint line illustration of the doctor"></div>
  <div class="about-frame abs"></div>
  <div class="about-photo abs" role="img" aria-label="Close-up portrait of Dr. Calvin Oberlake in thought"></div>
  <div class="about-text abs">
    <div class="eyebrow">About The Doctor:</div>
    <h3>Dr. Calvin Oberlake</h3>
    <p class="body-copy">Kestrel Valley Recovery Health Services (KVRHS) was conceptualized in 1985 when its founder Mr. Calvin D. Oberlake (Hartwell) was at the apex of his chemical dependency to heroin and alcohol which had culminated into a lifestyle of drug related offenses, incarceration and homelessness. He had come to the fork in the road in his life and had to make a decision between life and death! Little did he realize at that time that the beginning of his life would start at 'Rock Bottom'!</p>
  </div>
  <div class="signature abs" role="img" aria-label="Handwritten signature of Dr. Calvin Oberlake"></div>
</section>

<section class="book abs">
  <div class="book-text abs">
    <div class="eyebrow">About The Book:</div>
    <h3>Steady Ground After The Storm</h3>
    <p class="body-copy">Kestrel Valley Recovery Health Services (KVRHS) was conceptualized in 1985 when its founder Mr. Calvin D. Oberlake (Hartwell) was at the apex of his chemical dependency to heroin and alcohol which had culminated into a lifestyle of drug related offenses, incarceration and homelessness. He had come to the fork in the road in his life and had to make a decision between life and death! Little did he realize at that time that the beginning of his life would start at 'Rock Bottom'!</p>
  </div>
  <a href="#" class="btn book-btn abs">BUY NOW</a>
  <div class="book-visual abs" role="img" aria-label="Two copies of the book Steady Ground After The Storm lying on a table"></div>
</section>

<h2 class="blogs-title abs">Our Blogs</h2>
<div class="blogs-rule abs"></div>

<article class="blog-card abs" style="left:196px">
  <div class="blog-img" role="img" aria-label="Surgeons operating in a theatre" style="background:linear-gradient(180deg,#b9d3e6,#3f86b8)"></div>
  <h4>In our clinic discounts for a full inspection</h4>
  <p>Fummy text of the prnting and type news seting industrs standard known prin areter-took a printing and typenews...</p>
</article>
<article class="blog-card abs" style="left:479px">
  <div class="blog-img" role="img" aria-label="Scientist examining a test tube in a laboratory" style="background:linear-gradient(180deg,#9ccfc9,#e4efee)"></div>
  <h4>Medical Records are Safe Your now a days.</h4>
  <p>Fummy text of the prnting and type news seting industrs standard known prin areter-took a printing and typenews...</p>
</article>
<article class="blog-card abs" style="left:762px">
  <div class="blog-img" role="img" aria-label="Doctor reviewing records on a tablet" style="background:linear-gradient(90deg,#f1f1f1,#d9dde2)"></div>
  <h4>Office In our clinic discounts for a full inspection</h4>
  <p>Fummy text of the prnting and type news seting industrs standard known prin areter-took a printing and typenews...</p>
</article>

<footer class="site-footer abs">
  <div class="footer-brand abs"><span class="brand-dot"></span>Dr. Calvin Oberlake</div>
  <p class="footer-about abs">The name KVRHS grew out the unique relationship between Mr. Oberlake and his accountant, Mr. Martin Ashby as they talked about the concept of 'optimum quality behavioral healthcare and substance abuse services. Mr. Ashb...</p>
  <div class="footer-col abs" style="left:484px">
    <h5>Menu</h5>
    <ul><li>Meet The Doctor</li><li>The Book</li><li>Speaking</li><li>Consulting</li><li>Contact</li></ul>
  </div>
  <div class="footer-col abs" style="left:651px">
    <h5>Services</h5>
    <ul><li>Meet The Doctor</li><li>The Book</li><li>Speaking</li><li>Consulting</li><li>Contact</li></ul>
  </div>
  <div class="footer-col abs" style="left:812px">
    <h5>Contact Us</h5>
    <ul><li>Phone: 0198 732 640</li><li>Address: 48 Larkmoor Rd, Fenwick, NQ State</li></ul>
  </div>
</footer>
<div class="copyright abs">Copyright © 2019 DrCalvin.example</div>

</body>
</html>
```